Oven Cleaning flyer design

Hi there,
I need help designing a letterbox flyer. It needs to be DL size.
I have attached a rough design made with Chat GPT.
Would like back and front, have my business colors.
Please find attached mock up of what I would roughly like.
Also find attached logo.
Thank you

Target Market(s)

Home owners over 40

Industry/Entity Type

Cleaning

Requirements
Must have
• Logo, before after of oven, brand colors

```html
<!DOCTYPE html>
<html lang="en">
<head>
<meta charset="utf-8">
<title>Gleam Oven Care – DL Flyer Front and Back</title>
<link rel="stylesheet" href="https://fonts.googleapis.com/css2?family=Poppins:wght@400;500;600;700;800&family=Roboto+Condensed:wght@400;700;800&display=swap">
<style>
  :root{
    --navy:#1f2a5a;
    --navy-deep:#1a2450;
    --teal:#4cc3c8;
    --teal-soft:#7fd6d9;
    --ice:#eaf6f7;
    --white:#ffffff;
    --board:#d9dde0;
  }
  *{box-sizing:border-box;margin:0;padding:0}
  html,body{width:1200px;height:4894px;overflow:hidden}
  body{background:var(--board);position:relative;font-family:'Poppins',sans-serif}

  .flyer{position:absolute;left:243px;width:712px;height:1506px;overflow:hidden;background:var(--navy)}
  .flyer--front{top:1502px}
  .flyer--back{top:3110px}
  .layer{position:absolute;left:0;top:0}

  .brand{position:absolute;left:57px;top:66px;display:flex;align-items:center;gap:26px}
  .brand__dot{width:96px;height:96px;border-radius:50%;background:var(--teal)}
  .brand__name{font-family:'Poppins',sans-serif;font-weight:700;font-size:46px;letter-spacing:2px;color:var(--teal);line-height:1}

  .sparkle{position:absolute;color:var(--teal);font-size:26px;line-height:1}

  .headline{position:absolute;left:57px;top:228px;font-family:'Roboto Condensed',sans-serif;font-weight:800;font-size:70px;line-height:74px;color:var(--white);text-transform:uppercase}
  .headline em{font-style:normal;color:var(--teal)}
  .intro{position:absolute;left:57px;top:402px;width:532px;font-size:22px;line-height:35px;color:var(--white);text-align:justify}

  .compare{position:absolute;left:0;top:644px;width:712px;height:110px}
  .compare__label{position:absolute;top:0;height:110px;width:356px;display:flex;align-items:center;font-family:'Poppins',sans-serif;font-weight:700;font-size:54px;color:var(--white)}
  .compare__label--before{left:0;padding-left:50px;background:var(--navy)}
  .compare__label--after{left:356px;padding-left:88px;background:var(--teal)}
  .compare__arrow{position:absolute;left:324px;top:23px;width:64px;height:64px;border-radius:50%;background:var(--teal);border:3px solid var(--white)}

  .photo{position:absolute;top:754px;height:500px}
  .photo--before{left:0;width:355px;background:linear-gradient(180deg,#8b8f92 0%,#4a3b2c 45%,#7a5634 75%,#a77b52 100%)}
  .photo--after{left:359px;width:353px;background:linear-gradient(180deg,#9a9fa3 0%,#3d4143 45%,#6e5a44 75%,#a77b52 100%)}
  .photo-divider{position:absolute;left:355px;top:754px;width:4px;height:480px;background:var(--white)}
  .photo-seal{position:absolute;left:314px;top:1110px;width:86px;height:86px;border-radius:50%;background:var(--teal);border:5px solid var(--navy)}

  .cta{position:absolute;left:0;width:712px;text-align:center;color:var(--white)}
  .cta__lead{font-weight:700;font-size:58px;line-height:62px}
  .cta__sub{font-weight:400;font-size:33px;line-height:40px;letter-spacing:.5px}
  .cta__phone{font-weight:700;font-size:86px;line-height:100px;color:var(--teal);margin-top:4px}
  .cta__rule{width:470px;margin:4px auto 0;border-top:2px dashed var(--teal)}
  .cta__web{font-weight:500;font-size:38px;line-height:50px;color:var(--teal);margin-top:6px}
  .flyer--front .cta{top:1240px}
  .flyer--back .cta{top:1244px}

  .why{position:absolute;left:57px;top:222px;font-family:'Roboto Condensed',sans-serif;font-size:60px;line-height:68px;color:var(--white)}
  .why strong{display:block;font-weight:700;color:var(--teal);text-transform:uppercase}
  .why span{font-weight:400}
  .about{position:absolute;left:57px;top:356px;width:570px;font-size:21px;line-height:32px;color:var(--white);text-align:justify}

  .offer{position:absolute;left:72px;top:690px;width:566px;height:152px;border-radius:14px;background:var(--teal);display:flex;align-items:center;justify-content:center;font-family:'Roboto Condensed',sans-serif;font-weight:800;font-size:128px;color:var(--white);letter-spacing:2px}
  .offer-note{position:absolute;left:0;top:848px;width:712px;text-align:center;font-family:'Roboto Condensed',sans-serif;font-weight:800;font-size:70px;line-height:80px;color:var(--navy)}

  .perks{position:absolute;left:236px;top:962px;list-style:none}
  .perks li{display:flex;align-items:center;gap:22px;font-size:30px;line-height:45px;color:var(--navy);font-weight:500}
  .perks svg{flex:none}

  .extras{position:absolute;left:0;top:990px;width:210px;height:210px;border-radius:50%;background:var(--teal);display:flex;align-items:center;justify-content:center;text-align:center;font-family:'Roboto Condensed',sans-serif;font-size:35px;line-height:34px;color:var(--white)}
  .extras__mark{position:absolute;left:62px;top:920px;width:84px;height:84px;border-radius:50%;background:var(--teal);border:5px solid var(--navy)}
</style>
</head>
<body>

<!-- Front -->
<section class="flyer flyer--front">
  <svg class="layer" width="712" height="1506" viewBox="0 0 712 1506" aria-hidden="true">
    <rect width="712" height="1506" fill="var(--navy)"/>
    <path d="M0 600 C220 600 480 560 712 450 L712 644 L0 644 Z" fill="var(--teal)"/>
    <path d="M0 585 C230 592 480 548 712 430 L712 470 C480 580 230 620 0 618 Z" fill="var(--white)"/>
  </svg>

  <div class="brand"><span class="brand__dot"></span><span class="brand__name">GLEAM OVEN CARE</span></div>
  <span class="sparkle" style="left:540px;top:148px">✦</span>
  <span class="sparkle" style="left:30px;top:196px">✦</span>
  <span class="sparkle" style="left:490px;top:300px">✦</span>

  <h1 class="headline">Bring your <em>oven</em><br>back to life</h1>
  <p class="intro">Professional, non-caustic oven cleaning that removes built-up grease, smoke,and burnt grime - leaving your oven looking fresh again.</p>

  <div class="compare">
    <div class="compare__label compare__label--before">BEFORE</div>
    <div class="compare__label compare__label--after">AFTER</div>
    <svg class="compare__arrow" viewBox="0 0 64 64" aria-hidden="true">
      <circle cx="32" cy="32" r="18" fill="none" stroke="#fff" stroke-width="3"/>
      <path d="M22 32 H41 M34 25 L41 32 L34 39" fill="none" stroke="#fff" stroke-width="3.5" stroke-linecap="round" stroke-linejoin="round"/>
    </svg>
  </div>

  <div class="photo photo--before" role="img" aria-label="Photo of a dirty oven with burnt grime on the open door"></div>
  <div class="photo photo--after" role="img" aria-label="Photo of the same oven cleaned, door glass shining"></div>
  <div class="photo-divider"></div>

  <svg class="layer" style="top:1150px" width="712" height="356" viewBox="0 0 712 356" aria-hidden="true">
    <path d="M0 150 C200 40 500 20 712 40 L712 356 L0 356 Z" fill="var(--teal)"/>
    <path d="M0 190 C220 80 500 62 712 82 L712 356 L0 356 Z" fill="var(--navy)"/>
  </svg>
  <div class="photo-seal"></div>
  <span class="sparkle" style="left:452px;top:1170px;color:#fff">✦</span>
  <span class="sparkle" style="left:560px;top:1198px;color:#fff">✦</span>

  <div class="cta">
    <p class="cta__lead">CALL NOW FOR</p>
    <p class="cta__sub">FAST, PROFESSIONAL SERVICE</p>
    <p class="cta__phone">0400 555 182</p>
    <div class="cta__rule"></div>
    <p class="cta__web">gleamovencare.example</p>
  </div>
</section>

<!-- Back -->
<section class="flyer flyer--back" style="background:var(--ice)">
  <svg class="layer" width="712" height="1506" viewBox="0 0 712 1506" aria-hidden="true">
    <path d="M0 0 H712 V500 C520 580 260 600 0 560 Z" fill="var(--navy)"/>
    <path d="M0 560 C260 600 520 580 712 500 L712 530 C520 610 260 630 0 582 Z" fill="var(--white)"/>
    <path d="M0 582 C260 630 520 610 712 530 L712 548 C520 628 260 646 0 596 Z" fill="var(--teal)"/>
    <path d="M0 1226 C240 1150 480 1130 712 1148 L712 1506 L0 1506 Z" fill="var(--teal)"/>
    <path d="M0 1250 C240 1180 480 1164 712 1182 L712 1506 L0 1506 Z" fill="var(--navy)"/>
  </svg>

  <div class="brand"><span class="brand__dot"></span><span class="brand__name">GLEAM OVEN CARE</span></div>
  <span class="sparkle" style="left:30px;top:174px">✦</span>
  <span class="sparkle" style="left:470px;top:258px">✦</span>

  <h2 class="why"><span>Why Choose</span><strong>Gleam Oven Care?</strong></h2>
  <p class="about">We're a local family business providing professional, non-caustic oven cleaning across Sunshine Coast. Using specialized equipment and proven cleaning methods, we remove heavy grease, carbon build-up, smoke residue, restoring your oven safely and effectively.</p>

  <div class="offer">$10 OFF</div>
  <p class="offer-note">YOUR FIRST CLEAN</p>

  <ul class="perks">
    <li><svg width="22" height="22" viewBox="0 0 22 22" aria-hidden="true"><circle cx="11" cy="11" r="11" fill="var(--teal)"/><path d="M6 11.5 L9.5 15 L16 8" fill="none" stroke="#fff" stroke-width="2.6" stroke-linecap="round" stroke-linejoin="round"/></svg>Reliable Service</li>
    <li><svg width="22" height="22" viewBox="0 0 22 22" aria-hidden="true"><circle cx="11" cy="11" r="11" fill="var(--teal)"/><path d="M6 11.5 L9.5 15 L16 8" fill="none" stroke="#fff" stroke-width="2.6" stroke-linecap="round" stroke-linejoin="round"/></svg>Satisfaction Guaranteed</li>
    <li><svg width="22" height="22" viewBox="0 0 22 22" aria-hidden="true"><circle cx="11" cy="11" r="11" fill="var(--teal)"/><path d="M6 11.5 L9.5 15 L16 8" fill="none" stroke="#fff" stroke-width="2.6" stroke-linecap="round" stroke-linejoin="round"/></svg>Non-Caustic Cleaning</li>
  </ul>

  <div class="extras">We also clean<br>cooktops,<br>rangehoods<br>&amp; BBQs</div>
  <div class="extras__mark"></div>
  <span class="sparkle" style="left:360px;top:1120px">✦</span>
  <span class="sparkle" style="left:664px;top:1168px">✦</span>

  <div class="cta">
    <p class="cta__lead">CALL NOW FOR</p>
    <p class="cta__sub">FAST, PROFESSIONAL SERVICE</p>
    <p class="cta__phone">0400 555 182</p>
    <div class="cta__rule"></div>
    <p class="cta__web">gleamovencare.example</p>
  </div>
</section>

</body>
</html>
```